Lounge Night Poster

We need an attractive poster for our new lounge/night club in San Francisco called Velora Nightclub, promoting our new event, "Coral Night". We will have a live band and Asian singers performing during the night. It is like a lounge where people can chill and have a sip. It will open on July 21.

```html
<!DOCTYPE html>
<html lang="en">
<head>
<meta charset="utf-8">
<title>Coral Night — Velora Nightclub Poster</title>
<link rel="stylesheet" href="https://fonts.googleapis.com/css2?family=Poiret+One&family=Righteous&family=Space+Mono:wght@700&display=swap">
<style>
  :root {
    --stage: #063a4f;
    --night: #0b0b12;
    --violet: #5a2d9c;
    --magenta: #d8308f;
    --lilac: #c9a6e6;
    --red: #e0160e;
    --deep-red: #c10d0a;
    --orange: #ff8a12;
    --white: #ffffff;
    --yellow: #f2dd1c;
  }
  * { box-sizing: border-box; margin: 0; padding: 0; }
  html, body {
    width: 1200px;
    height: 900px;
    overflow: hidden;
    background: var(--stage);
  }
  .canvas {
    position: relative;
    width: 1200px;
    height: 900px;
    background: var(--stage);
  }
  .poster {
    position: absolute;
    left: 311px;
    top: 40px;
    width: 578px;
    height: 820px;
    overflow: hidden;
    background: var(--night);
  }
  .light-dots {
    position: absolute;
    left: 0;
    top: 0;
    width: 100%;
    height: 300px;
    background: linear-gradient(180deg,
      var(--magenta) 0%,
      var(--lilac) 22%,
      var(--violet) 50%,
      rgba(11, 11, 18, 0.9) 72%,
      rgba(60, 35, 125, 0.8) 100%);
  }
  .crowd {
    position: absolute;
    left: 0;
    top: 300px;
    width: 100%;
    height: 520px;
    background: linear-gradient(180deg,
      rgba(60, 35, 125, 0.8) 0%,
      var(--deep-red) 18%,
      var(--red) 45%,
      #e8340f 62%,
      var(--red) 80%,
      var(--deep-red) 100%);
  }
  .event-title {
    position: absolute;
    left: 0;
    top: 198px;
    width: 100%;
    text-align: center;
    font-family: "Poiret One", sans-serif;
    font-weight: 400;
    font-size: 64px;
    line-height: 1;
    letter-spacing: 1px;
    color: var(--white);
  }
  .event-title .accent { color: var(--yellow); }
  .venue {
    position: absolute;
    left: 0;
    top: 680px;
    width: 100%;
    text-align: center;
    font-family: "Righteous", sans-serif;
    font-size: 43px;
    line-height: 1;
    letter-spacing: 1px;
    color: var(--white);
  }
  .opening {
    position: absolute;
    left: 0;
    top: 734px;
    width: 100%;
    text-align: center;
    font-family: "Space Mono", monospace;
    font-weight: 700;
    font-size: 26px;
    line-height: 1;
    letter-spacing: 3px;
    color: var(--yellow);
  }
</style>
</head>
<body>
  <main class="canvas">
    <section class="poster">
      <div class="light-dots" role="img" aria-label="Disco light dot pattern in pink, white and violet with sparkles"></div>
      <div class="crowd" role="img" aria-label="Red dancing crowd with raised hands over orange light dots"></div>
      <h1 class="event-title">CORAL <span class="accent">NIGHT</span></h1>
      <p class="venue">VELORA NIGHTCLUB</p>
      <p class="opening">it will open on July 21</p>
    </section>
  </main>
</body>
</html>
```